Doctors Office Web Design

Name of the business is Lin-Yue Hart M.D.
We need a web design that is attractive for women that want to see Dr. Lin-Yue Hart for Obstetrician Gynecology and Pregnancy care. Dr. Hart earned her degree from Carrow Ridge Medical College of obstetrician gynecology. We want to attract women of child bearing ages to come to our offices for health, education, and pregnancies.

Please visit http://www.drhartclinicweb.com/ to help you get a feel for who we are. We will be adding some pictures and logo in the next few days.

We are looking for to have pages for and tabs including
About Us- History, Our Staff, Dr. Hart
Patient Information- Appointments, E-Prescriptions, Payments Accepted, Insurance
Health- General, Sexual, Mental, Affiliates
Pregnancy- Minimally invasive surgery(our specialty), 4-D Ultra Sound, Hospital Affiliations
Media- News,Pictures, Videos
Locations- Palmer Office, Westvale Office

The colors we would like to use are pastel colors, magenta, and plum

Target Market(s)

Women of all ages with an emphasis on 25-65 year olds

Industry/Entity Type

Business

Requirements
Must have
• Needs to include a location for a our videos and pictures that I will submit shortly. We also want a map to our location or atleast a place for one.
Nice to have
• A place for a google map of our office locations.

```html
<!DOCTYPE html>
<html lang="en">
<head>
<meta charset="utf-8">
<title>Lin-Yue Hart M.D.</title>
<link href="https://fonts.googleapis.com/css2?family=PT+Sans:wght@400;700&family=Didact+Gothic&family=Arimo&display=swap" rel="stylesheet">
<style>
:root{
  --magenta:#9a0c62;
  --nav-top:#d2249a;
  --nav-bottom:#b80f83;
  --logo-pink:#c7609b;
  --plum-text:#6a3a8c;
  --heading-pink:#c8309a;
  --link-crimson:#a3005c;
  --plum-title:#8a0c5c;
  --link-pink:#d0308f;
  --ink:#222;
  --body:#444;
  --rule:#dcdcdc;
  --footer:#a9a9a9;
  --panel:#f6f6f6;
}
*{margin:0;padding:0;box-sizing:border-box}
html,body{width:1005px;height:1200px;overflow:hidden}
body{position:relative;background:#fff;font-family:"PT Sans",sans-serif;color:var(--body)}
.band-top{position:absolute;left:0;top:0;width:1005px;height:538px;background:var(--magenta)}
.band-footer{position:absolute;left:0;top:1124px;width:1005px;height:76px;background:var(--footer)}
.page{position:absolute;left:37px;top:23px;width:945px;height:1126px;background:#fff}
.abs{position:absolute}

.logo-name{left:26px;top:26px;font-weight:700;font-size:33px;color:var(--logo-pink);letter-spacing:.2px}
.logo-title{left:198px;top:67px;font-size:16px;color:var(--plum-text)}
.search{left:746px;top:40px;width:180px;height:29px;border:1px solid var(--rule);display:flex;font-size:15px;color:#444}
.search span{flex:1;padding:5px 0 0 13px}
.search b{width:45px;background:#eee;border-left:1px solid var(--rule);font-weight:400;text-align:center;padding-top:5px}

.nav{left:17px;top:100px;width:912px;height:43px;background:linear-gradient(var(--nav-top),var(--nav-bottom));display:flex;list-style:none}
.nav li{height:43px;border-right:1px solid rgba(255,255,255,.45);color:#fff;font-family:"Arimo",sans-serif;font-size:13.5px;text-transform:uppercase;text-align:center;line-height:46px}

.hero{left:19px;top:161px;width:907px;height:326px;border:1px solid #ccc;background:#f2f2f2;overflow:hidden}
.hero-photo{position:absolute;left:0;top:0;width:907px;height:326px;background:linear-gradient(90deg,#e9e3dc 0%,#f4f0ec 35%,#eeeeee 55%,#e4e6ea 80%,#b9c2cc 100%)}
.hero-heading{left:497px;top:36px;font-family:"Didact Gothic",sans-serif;font-size:33px;color:var(--heading-pink);letter-spacing:.4px;font-weight:700;white-space:nowrap}
.hero-text{left:498px;top:94px;width:395px;font-size:17px;line-height:21px;color:#111}
.btn{left:752px;top:223px;width:113px;height:31px;background:#c35aa0;border:1px solid #a9468a;color:#fff;font-size:15px;line-height:29px;padding-left:15px}
.btn svg{position:absolute;right:12px;top:11px}
.dots{left:740px;top:304px;width:168px;height:22px;background:#eee;display:flex;gap:5px;padding:6px 0 0 10px}
.dots i{width:11px;height:11px;border-radius:50%;background:#fff;border:1px solid #999}
.dots i.on{background:#a0448a;border-color:#a0448a}

.thumb{top:516px;width:283px;height:169px;background:#ddd;padding:4px}
.thumb .fill{width:100%;height:100%}
.col-title{top:696px;font-size:19px;color:var(--ink)}
.col-title.pink{color:var(--heading-pink)}
.col-text{top:726px;width:292px;font-size:12.5px;line-height:21px;color:#444}
.col-link{font-size:12.5px;color:var(--link-crimson)}

.services{left:20px;top:864px;width:910px;height:62px;background:var(--panel);border:1px solid var(--rule)}
.services .lead{position:absolute;left:16px;top:19px;font-size:18px;color:#333}
.services .phone{position:absolute;left:282px;top:20px;font-size:16px;color:#222;display:flex;gap:14px;align-items:center}
.services .quote{position:absolute;left:482px;top:12px;width:420px;font-size:12px;line-height:21px;color:#444}
.services .quote em{font-style:normal;color:var(--link-pink)}

.svc-title{top:960px;font-size:19px;font-weight:700;color:var(--plum-title)}
.svc-text{top:993px;width:280px;font-size:12px;line-height:21px;color:#444}
.svc-link{font-size:12px;color:var(--link-pink)}

.social{left:36px;top:1172px;display:flex;gap:8px;font-size:11px;color:#fff}
.social span{display:flex;align-items:center;gap:4px}
.social i{width:9px;height:9px;background:#3a5a99;display:block}
.copyright{left:744px;top:1173px;font-size:12px;color:#fff}
</style>
</head>
<body>
<div class="band-top"></div>
<div class="band-footer"></div>

<div class="page">
  <div class="abs logo-name">Lin-Yue Hart</div>
  <div class="abs logo-title">M.D.</div>
  <div class="abs search"><span>Search</span><b>Go</b></div>

  <ul class="abs nav">
    <li style="width:68px">Home</li>
    <li style="width:116px">About Us</li>
    <li style="width:202px">Patient Information</li>
    <li style="width:105px">Health</li>
    <li style="width:133px">Pregnancy</li>
    <li style="width:95px">Media</li>
    <li style="width:124px">Locations</li>
  </ul>

  <div class="abs hero">
    <div class="hero-photo" role="img" aria-label="Smiling medical team in white coats with a stethoscope"></div>
    <div class="abs hero-heading">Complete Heath Solution</div>
    <p class="abs hero-text">Lorem ipsum dolor sit ipsum Lorem ipsum dolor sit ipsumLorem ipsum dolor sit ipsumLorem ipsum dolor sit ipsumLorem ipsum dolor sit ipsumLorem ipsum dolor sit ipsumLorem ipsum dolor sit ipsumLorem ipsum dolor sit ipsum</p>
    <div class="abs btn">Read More
      <svg width="7" height="9" viewBox="0 0 7 9"><path d="M1 1l4 3.5L1 8" stroke="#fff" stroke-width="2" fill="none"/></svg>
    </div>
    <div class="abs dots"><i></i><i></i><i class="on"></i><i></i><i></i><i></i><i></i></div>
  </div>

  <div class="abs thumb" style="left:19px"><div class="fill" role="img" aria-label="Group of smiling clinic staff" style="background:linear-gradient(90deg,#c9d6e4,#eef2f6 50%,#cfdbe8)"></div></div>
  <div class="abs thumb" style="left:331px"><div class="fill" role="img" aria-label="Map of office locations along the coast" style="background:linear-gradient(90deg,#efe7cf 0%,#f2ecd8 60%,#a9c5e4 68%,#a9c5e4 100%)"></div></div>
  <div class="abs thumb" style="left:644px;background:#e8e8e8;border:1px solid #ccc">
    <div class="fill" role="img" aria-label="Ultrasound video still" style="height:138px;background:radial-gradient(ellipse at 40% 55%,#8a8a8a,#2a2a2a 60%,#111)"></div>
    <svg class="abs" style="left:4px;top:147px" width="272" height="22" viewBox="0 0 272 22">
      <circle cx="12" cy="11" r="10" fill="#fff" stroke="#bbb"/>
      <path d="M9 6l8 5-8 5z" fill="#c8309a"/>
      <rect x="30" y="6" width="200" height="10" fill="#fff" stroke="#aaa"/>
      <rect x="36" y="7" width="5" height="8" fill="#c8309a"/>
      <text x="236" y="14" font-size="6.5" fill="#333" font-family="Arimo,sans-serif">0:00 / 0:00</text>
    </svg>
  </div>

  <div class="abs col-title pink" style="left:30px">About us</div>
  <p class="abs col-text" style="left:30px">Lorem ipsum dolor sit ipsum Lorem ipsum dolor sit ipsumLorem ipsum dolor sit ipsumLorem ipsum dolor sit ipsumLorem ipsum dolor sit ipsumLorem ipsum dolor sit ipsum<br><span class="col-link" style="line-height:38px">Read More</span></p>

  <div class="abs col-title" style="left:331px;top:694px">Our Locations</div>
  <p class="abs col-text" style="left:332px;top:724px">Lorem ipsum dolor sit ipsum Lorem ipsum dolor sit ipsumLorem ipsum dolor sit ipsumLorem ipsum dolor sit ipsumLorem ipsum dolor sit ipsumLorem ipsum dolor sit ipsum<br><span class="col-link" style="line-height:38px">Read More</span></p>

  <div class="abs col-title" style="left:644px;top:694px">Our Video</div>
  <p class="abs col-text" style="left:644px;top:723px">Lorem ipsum dolor sit ipsum Lorem ipsum dolor sit ipsumLorem ipsum dolor sit ipsumLorem ipsum dolor sit ipsumLorem ipsum dolor sit ipsumLorem ipsum dolor sit ipsum<br><span class="col-link" style="line-height:38px">Read More</span></p>

  <div class="abs services">
    <div class="lead">If you require our services :</div>
    <div class="phone">
      <svg width="22" height="16" viewBox="0 0 22 16"><path d="M2 6c0-4 18-4 18 0v2h-5V5H7v3H2z" fill="#333"/><path d="M5 9h12l2 6H3z" fill="#333"/><circle cx="11" cy="12" r="2" fill="#f6f6f6"/></svg>
      248. 306. 91570
    </div>
    <p class="quote">“Lorem Ipsum dolor sit ipsum Lorem Ipsum dolor sit ipsum Lorem Ipsum dolor sit ipsum Lorem Ipsum dolor sit ipsum Lorem Ipsum dolor sit ipsum” <em>Client says</em></p>
  </div>

  <div class="abs svc-title" style="left:20px">Obstetrics</div>
  <p class="abs svc-text" style="left:20px">Donec mollis, tellus id congue blandit, urna tellus vestibulum risus, ac luctus urna risus ac neque. Nam sed nisl eget lacus rhoncus cursus. Nam sem nisi, sodales sit amet interdum et, commodo vel eros.<br><span class="svc-link" style="line-height:38px">Read More &gt;&gt;</span></p>

  <div class="abs svc-title" style="left:331px">Family Planning</div>
  <p class="abs svc-text" style="left:331px">Donec mollis, tellus id congue blandit, urna tellus vestibulum risus, ac luctus urna risus ac neque. Nam sed nisl eget lacus rhoncus cursus. Nam sem nisi, sodales sit amet interdum et, commodo vel eros.<br><span class="svc-link" style="line-height:38px">Read More &gt;&gt;</span></p>

  <div class="abs svc-title" style="left:644px">Hormonal Evaluation</div>
  <p class="abs svc-text" style="left:644px">Donec mollis, tellus id congue blandit, urna tellus vestibulum risus, ac luctus urna risus ac neque. Nam sed nisl eget lacus rhoncus cursus. Nam sem nisi, sodales sit amet interdum et, commodo vel eros.<br><span class="svc-link" style="line-height:38px">Read More &gt;&gt;</span></p>
</div>

<div class="abs social">
  <span><i></i>Pagebook</span>
  <span><i></i>Chirper</span>
  <span><i></i>WorkNet</span>
</div>
<div class="abs copyright">Copyright © 2011 All Rights Reserved LINHA</div>
</body>
</html>
```